Thrifty and Thriving Personal Finance Character

This is a title of a course that I work through with my personal finance coaching clients. I need a banner for content section and a mascot character. I am thinking a fun owl with some sort of financial twist. Would like to use emerald green background and complimenting colors. My website is www.harborlanemoneyguides.com

I will need five variants one mascot is chosen

1) Owl driving car (signifies Wise car purchases)
2) Owl and house (signifies Wise car purchases)
3) Owl and graduate cap (signifies Wise college planning)
4) Owl and stocks, bonds, investments (signifies Wise investing)
5) Owl saving money maybe with piggy bank (signifies Wise savings)

Target Market(s)

Young professional, couples and families

Industry/Entity Type

Personal Finance Coaching

Font styles to use
Serif

Colors
00AB8E
00BBA5
67D7C9
C6EFE9
E9F9F6

Requirements
Must have
• Owl fun character with some tie to money
Should not have
• Not formal

```html
<!DOCTYPE html>
<html lang="en">
<head>
<meta charset="utf-8">
<title>Thrifty and Thriving Personal Finance Character – Content Banners</title>
<link rel="stylesheet" href="https://fonts.googleapis.com/css2?family=Cinzel:wght@700&display=swap">
<style>
  :root {
    --page: #ffffff;
    --emerald-light: #00cc9c;
    --emerald: #00ab8e;
    --emerald-deep: #00916f;
    --floor: #00c49a;
    --gold: #c99a3a;
    --gold-light: #e0b860;
    --navy: #0b2a55;
    --title: #ffffff;
  }
  * { box-sizing: border-box; margin: 0; padding: 0; }
  html, body {
    width: 1200px;
    height: 2280px;
    overflow: hidden;
    background: var(--page);
  }
  .banner-set {
    width: 1200px;
    height: 2280px;
    padding-top: 65px;
    display: flex;
    flex-direction: column;
    align-items: center;
    gap: 13px;
  }
  .banner {
    position: relative;
    width: 1020px;
    height: 420px;
    overflow: hidden;
    background: linear-gradient(200deg, var(--emerald-light) 0%, var(--emerald) 45%, var(--emerald-deep) 100%);
  }
  .banner-floor {
    position: absolute;
    inset: 0;
    width: 100%;
    height: 100%;
  }
  .mascot-scene {
    position: absolute;
    top: 30px;
    width: 300px;
    height: 370px;
    border-radius: 36px;
    background: linear-gradient(180deg, var(--gold-light) 0%, var(--gold) 38%, var(--navy) 100%);
  }
  .scene-college   { left: 110px; }
  .scene-savings   { left: 30px;  width: 400px; }
  .scene-car       { left: 30px;  width: 480px; }
  .scene-house     { left: 30px;  width: 480px; }
  .scene-investing { left: 30px;  width: 450px; }
  .banner-title {
    position: absolute;
    left: 544px;
    top: 0;
    height: 100%;
    display: flex;
    flex-direction: column;
    justify-content: center;
    font-family: "Cinzel", "Times New Roman", serif;
    font-weight: 700;
    font-size: 84px;
    line-height: 97px;
    color: var(--title);
  }
  .title-line { display: block; white-space: nowrap; }
  .title-line .rest { font-size: 68px; }
</style>
</head>
<body>
<main class="banner-set">

  <section class="banner">
    <svg class="banner-floor" viewBox="0 0 1020 420" preserveAspectRatio="none" aria-hidden="true">
      <polygon points="0,40 1020,0 1020,420 1000,420 420,340 60,330" fill="#00916f" opacity="0.35"/>
      <polygon points="60,340 420,340 1020,420 0,420 0,340" fill="#00c49a"/>
    </svg>
    <div class="mascot-scene scene-college" role="img" aria-label="Gold and navy owl mascot in a graduation cap, with white line drawings of diploma scrolls behind it"></div>
    <h2 class="banner-title"><span class="title-line">W<span class="rest">ise</span></span><span class="title-line">C<span class="rest">ollege</span></span><span class="title-line">P<span class="rest">lanning</span></span></h2>
  </section>

  <section class="banner">
    <svg class="banner-floor" viewBox="0 0 1020 420" preserveAspectRatio="none" aria-hidden="true">
      <polygon points="0,40 1020,0 1020,420 1000,420 420,340 60,330" fill="#00916f" opacity="0.35"/>
      <polygon points="60,340 420,340 1020,420 0,420 0,340" fill="#00c49a"/>
    </svg>
    <div class="mascot-scene scene-savings" role="img" aria-label="Gold and navy owl mascot dropping dollar coins into a mint green piggy bank"></div>
    <h2 class="banner-title"><span class="title-line">W<span class="rest">ise</span></span><span class="title-line">S<span class="rest">avings</span></span></h2>
  </section>

  <section class="banner">
    <svg class="banner-floor" viewBox="0 0 1020 420" preserveAspectRatio="none" aria-hidden="true">
      <polygon points="0,40 1020,0 1020,420 1000,420 420,340 60,330" fill="#00916f" opacity="0.35"/>
      <polygon points="60,340 420,340 1020,420 0,420 0,340" fill="#00c49a"/>
    </svg>
    <div class="mascot-scene scene-car" role="img" aria-label="Gold and navy owl mascot holding car keys in front of a white line drawing of a classic car"></div>
    <h2 class="banner-title"><span class="title-line">W<span class="rest">ise</span></span><span class="title-line">C<span class="rest">ar</span></span><span class="title-line">P<span class="rest">urchases</span></span></h2>
  </section>

  <section class="banner">
    <svg class="banner-floor" viewBox="0 0 1020 420" preserveAspectRatio="none" aria-hidden="true">
      <polygon points="0,40 1020,0 1020,420 1000,420 420,340 60,330" fill="#00916f" opacity="0.35"/>
      <polygon points="60,340 420,340 1020,420 0,420 0,340" fill="#00c49a"/>
    </svg>
    <div class="mascot-scene scene-house" role="img" aria-label="Gold and navy owl mascot holding a house key in front of a white line drawing of a house"></div>
    <h2 class="banner-title"><span class="title-line">W<span class="rest">ise</span></span><span class="title-line">H<span class="rest">ouse</span></span><span class="title-line">P<span class="rest">urchases</span></span></h2>
  </section>

  <section class="banner">
    <svg class="banner-floor" viewBox="0 0 1020 420" preserveAspectRatio="none" aria-hidden="true">
      <polygon points="0,40 1020,0 1020,420 1000,420 420,340 60,330" fill="#00916f" opacity="0.35"/>
      <polygon points="60,340 420,340 1020,420 0,420 0,340" fill="#00c49a"/>
    </svg>
    <div class="mascot-scene scene-investing" role="img" aria-label="Gold and navy owl mascot in front of white line drawings of stock charts, coins, plants and a rising arrow"></div>
    <h2 class="banner-title"><span class="title-line">W<span class="rest">ise</span></span><span class="title-line">I<span class="rest">nvesting</span></span></h2>
  </section>

</main>
</body>
</html>
```